Copper Lantern Coffee Bean Labels

We need a label for a new brand of coffee that we are selling in Portland, Oregon (Coffee Capital). Our company has no current online presence but have some great roasting techniques. We will be roasting our own coffee beans from throughout the world and selling them immediately after roasting causing a super fresh and high quality product.

We will be packaging in brown kraft bags: 3 3/8 X 2.5 x 7.75 inches which is standard for coffee beans.

Also notice on that sample the blue section in the middle has the product name. We want to also make it so that there is a consistent area that we can print OVER the label the name or blend of the coffee.

Our company is called Copper Lantern Coffee Roasters. We will want to put copperlanternroasters.example on the label someplace (we dont have a site yet but will by launch).

We need to incorporate A Black Diamond into the design. No preferences yet on the style of it.

We want to be a super-premium brand. Sort of like MicroBrew beers. We will sell at Farmers Markets, online, and directly into stores. Image is very important to us.

Labels should be about 3" wide and about 3.75" high.. Perhaps higher if a cool design justifies the height. Again we will be using a brown kraft bag (like grocery bag color) as shown on the sample.

SEE ATTACHED SEVERAL INTERESTING DESIGNS

Target Market(s)

Foodies, Yuppie, Coffee Snob

Industry/Entity Type

It Company

Requirements
Must have
• Location for the product Name to go onto it... We want to use the same labels for our full line. Just printing over it something like "Italian Roast" and a line below saying something like "Bold, Nutty Flavor, blah blah"

Should not have
• Clunkey looking old fonts or things that look homemade.

```html
<!DOCTYPE html>
<html lang="en">
<head>
<meta charset="utf-8">
<title>Copper Lantern Coffee Roasters – House Blend Label</title>
<link rel="stylesheet" href="https://fonts.googleapis.com/css2?family=Ubuntu:wght@400;500;700&display=swap">
<style>
  :root {
    --page-bg: #ece9e4;
    --label-paper: #ffffff;
    --damask-tone: #f3f2ef;
    --burst-center: #e4e2de;
    --gold-band: #a8861a;
    --logo-ink: #1c1a19;
    --blend-brown: #9a5a17;
    --detail-ink: #5e4a36;
    --rule-ink: #3a3028;
    --url-copper: #a65a1c;
  }
  * { box-sizing: border-box; margin: 0; padding: 0; }
  html, body {
    width: 722px;
    height: 1200px;
    overflow: hidden;
    background: var(--page-bg);
    font-family: "Ubuntu", sans-serif;
  }
  .label {
    position: absolute;
    left: 51px;
    top: 208px;
    width: 620px;
    height: 784px;
    background: var(--label-paper);
    box-shadow: 0 2px 10px rgba(0,0,0,0.12);
    overflow: hidden;
  }
  .band {
    position: absolute;
    left: 0;
    width: 100%;
    height: 26px;
    background: var(--gold-band);
  }
  .band--top { top: 0; }
  .band--bottom { bottom: 0; }
  .damask-field {
    position: absolute;
    left: 0; top: 26px;
    width: 100%;
    height: calc(100% - 52px);
    background: var(--damask-tone);
  }
  .sunburst {
    position: absolute;
    left: 20px;
    top: 60px;
    width: 580px;
    height: 470px;
    border-radius: 50%;
    background: radial-gradient(ellipse at center, var(--burst-center) 0%, rgba(228,226,222,0.6) 45%, rgba(243,242,239,0) 72%);
  }
  .brand-name {
    position: absolute;
    left: 0;
    top: 230px;
    width: 100%;
    text-align: center;
    font-weight: 500;
    font-size: 64px;
    line-height: 72px;
    color: var(--logo-ink);
    letter-spacing: -1px;
  }
  .product {
    position: absolute;
    left: 104px;
    top: 556px;
    display: flex;
    align-items: stretch;
  }
  .product__name {
    font-weight: 700;
    font-size: 50px;
    line-height: 54px;
    color: var(--blend-brown);
    letter-spacing: 1px;
    padding-right: 16px;
    border-right: 3px solid var(--rule-ink);
  }
  .product__notes {
    padding-left: 14px;
    padding-top: 4px;
    font-size: 27px;
    line-height: 34px;
    color: var(--detail-ink);
  }
  .web-address {
    position: absolute;
    left: 0;
    top: 706px;
    width: 100%;
    text-align: center;
    font-size: 23px;
    font-weight: 500;
    color: var(--url-copper);
  }
</style>
</head>
<body>
  <main class="label">
    <div class="band band--top"></div>
    <div class="damask-field" role="img" aria-label="Faint grey damask pattern covering the label background"></div>
    <div class="sunburst" role="img" aria-label="Radiating sunburst rays behind the brand name"></div>
    <h1 class="brand-name">Copper Lantern<br>Coffee Roasters</h1>
    <section class="product">
      <h2 class="product__name">HOUSE<br>BLEND</h2>
      <p class="product__notes">Ground Coffee<br>Nutty Flavor</p>
    </section>
    <p class="web-address">www.copperlanternroasters.example</p>
    <div class="band band--bottom"></div>
  </main>
</body>
</html>
```